User help guide for software for investment bank

We need a professional design for our user help guides for new software we have written for our client. We develop visualization software for investment banks in Singapore mainly focused in the financial and risk management area. Our help guides are design to show them how the software works as well as promote our brand
Updates

Target Market(s)

Investment banking, risk management, finance

Industry/Entity Type

Bank

Requirements
Must have
• Content of document and logos
• Colour sheme
• Professional brouchure design
• Verindo and plunox logos on it
• Look at www.verindo-example.com for company looks and feel
• PLEASE USE COLOUR SCHEMES BELOW IN ATTACHMENT AND FOLLOW SIMILAR STYLE TO CLIENT ANNUAL REPORT

```html
<!DOCTYPE html>
<html lang="en">
<head>
<meta charset="utf-8">
<title>Verindo User Guide – Navigation</title>
<link href="https://fonts.googleapis.com/css2?family=Open+Sans:wght@400;600;700&display=swap" rel="stylesheet">
<style>
:root{
  --blue:#1c6ea4;
  --green:#3d9b2f;
  --ink:#4a4a4a;
  --paper:#ffffff;
  --bg:#ffffff;
  --frame:#2d6fb4;
  --ui-bg:#f3f6f9;
  --ui-line:#d5dde6;
  --ui-head:#c9d8e8;
  --ui-side:#e4ebf2;
  --band-blue:#bcd3e6;
  --band-mid:#e3ecf2;
  --band-green:#d3e6c8;
}
*{margin:0;padding:0;box-sizing:border-box}
html,body{width:840px;height:1200px;overflow:hidden;background:var(--bg)}
body{position:relative;font-family:"Open Sans",Arial,sans-serif;color:var(--ink)}
.spread{position:absolute;left:19px;width:792px;background:var(--paper);box-shadow:4px 6px 10px rgba(0,0,0,.35);overflow:hidden}
.spread--top{top:14px;height:565px}
.spread--bottom{top:614px;height:567px}
.footer-band{position:absolute;left:0;bottom:0;width:100%;height:100px;
  background:linear-gradient(90deg,var(--band-blue),var(--band-mid) 50%,var(--band-green))}
.footer-band::after{content:"";position:absolute;inset:0;
  background:linear-gradient(180deg,#fff 0%,rgba(255,255,255,.6) 45%,rgba(255,255,255,0) 100%)}
.page-num{position:absolute;width:12px;height:12px;color:#fff;font-size:8px;font-weight:700;text-align:center;line-height:12px;z-index:2}
.page-num--blue{background:var(--blue)}
.page-num--green{background:#7cb85a}
.blk{position:absolute;font-size:6.9px;line-height:9.6px}
.blk p{margin-bottom:9.6px}
.blk p.tight{margin-bottom:0}
.blk--loose p{margin-bottom:13.5px}
h2.section{position:absolute;font-size:11px;font-weight:700;color:var(--blue)}
h3.sub{font-size:8.2px;font-weight:700;color:var(--blue);margin-bottom:2px}
h4.minor{font-size:7px;font-weight:600;color:var(--blue);margin:0 0 0 18px}
.g{color:var(--green);font-weight:600}
ul.list{list-style:none;margin-left:12px}
ul.list li::before{content:"• ";color:var(--green);font-weight:700}

/* UI screenshot areas */
.shot{position:absolute;border:1px solid var(--frame);background:var(--ui-bg);overflow:hidden}
.shot--app{
  background:
    linear-gradient(var(--ui-head),var(--ui-head)) 0 0/100% 9px no-repeat,
    linear-gradient(var(--ui-side),var(--ui-side)) 0 9px/42px 100% no-repeat,
    linear-gradient(#eef2f6,#eef2f6) 42px 9px/48px 100% no-repeat,
    repeating-linear-gradient(180deg,transparent 0 7px,var(--ui-line) 7px 8px) 0 26px/100% 100% no-repeat,
    var(--ui-bg)}
.shot--app::before{content:"";position:absolute;left:91px;top:18px;right:4px;height:4px;background:#b8cce0}
.shot--app::after{content:"";position:absolute;left:0;right:0;bottom:0;height:6px;background:#dfe6ee;border-top:1px solid var(--ui-line)}
.shot--list{
  background:
    linear-gradient(var(--ui-head),var(--ui-head)) 0 0/100% 7px no-repeat,
    repeating-linear-gradient(180deg,transparent 0 6px,var(--ui-line) 6px 7px) 0 7px/100% 100% no-repeat,
    #fff}
.shot--menu{
  background:
    linear-gradient(var(--ui-head),var(--ui-head)) 0 0/100% 8px no-repeat,
    linear-gradient(#eef2f6,#eef2f6) 0 8px/45% 100% no-repeat,
    repeating-linear-gradient(180deg,transparent 0 10px,var(--ui-line) 10px 11px) 0 8px/100% 100% no-repeat,
    #fff}
.hl{position:absolute;border:1px solid #e58a2e;border-radius:4px}
.label{position:absolute;font-size:8.2px;font-weight:700;color:var(--blue)}
.edit-bar{position:absolute;left:138px;top:80px;width:123px;height:20px;border:1px solid var(--frame);display:flex;align-items:center;gap:8px;padding-left:6px;font-size:5px;color:#555}
.edit-bar .edit{border:1.2px solid #e11;border-radius:50%;padding:1px 5px}
.toolbar{position:absolute;left:27px;top:62px;width:292px;height:16px;border:1px solid var(--frame);
  background:repeating-linear-gradient(90deg,transparent 0 14px,#c3cfdc 14px 20px,transparent 20px 26px) 8px 4px/200px 6px no-repeat,#f4f6f8}
</style>
</head>
<body>

<!-- Spread: pages 4 and 5 -->
<section class="spread spread--top">
  <div class="footer-band" role="img" aria-label="Soft band in light blue and green"></div>

  <h2 class="section" style="left:27px;top:38px">3. Navigation</h2>
  <div class="blk" style="left:27px;top:62px;width:364px">
    <p>The users can access to the Web Editing Tool by clicking on the “Edit” button that is placed at the bottom of the current Report.</p>
  </div>
  <div class="edit-bar"><span>➦ Share</span><span>Remember my changes</span><span class="edit">Edit</span></div>
  <div class="blk" style="left:27px;top:121px;width:364px">
    <p>When the user clicks on this button, the Web Editing Tool is activated and the user can see the screen below (We fully recommend to use Orbit Browser for the editing tool):</p>
  </div>
  <div class="shot shot--app" style="left:53px;top:142px;width:293px;height:166px" role="img" aria-label="Screenshot of the NRMF Actuals report builder in the web editor"></div>
  <div class="blk" style="left:27px;top:324px;width:364px">
    <p>These are the different areas included at the Web Editor, there is below a full summary for all the areas included at the Wed Editing Tool.</p>
  </div>
  <div class="blk" style="left:27px;top:351px;width:364px">
    <h3 class="sub">a.&nbsp; Data and Analytics pane.</h3>
    <p>This area appears on the left side of the workspace and is divided in 2 tabs: Data and Analytics</p>
  </div>
  <div class="shot shot--list" style="left:177px;top:376px;width:64px;height:142px" role="img" aria-label="Screenshot of the data pane field list"></div>
  <div class="shot shot--list" style="left:221px;top:466px;width:35px;height:52px" role="img" aria-label="Screenshot of the analytics pane"></div>
  <div class="page-num page-num--blue" style="left:356px;top:518px">4</div>

  <div class="blk" style="left:421px;top:39px;width:355px">
    <p>The data pane include the names of the data sources included on the workbook, and the fields (as dimension or measure), parameters, and sets included in the active data source.</p>
    <p>The active data source will be always the source that appears with a blue arrow. If the user clicks in other data source, the Data pane will change and will show the fields, parameters, and sets included at the clicked data source.</p>
    <p>For NRMF there are some fields and data sources that have been used for internal purposes and have not business containing, they have the __PROGRAM prefix. If the user access to them, maybe will find not understanding fields but they are used for create rest of fields and measures used at reports.</p>
  </div>
  <div class="shot shot--list" style="left:546px;top:146px;width:94px;height:108px" role="img" aria-label="Screenshot of data sources with program prefixed items highlighted">
    <div class="hl" style="left:1px;top:7px;width:90px;height:36px"></div>
    <div class="hl" style="left:1px;top:86px;width:90px;height:14px"></div>
  </div>
  <div class="blk" style="left:421px;top:273px;width:355px">
    <p class="tight">The pane is split in 2 parts: Data Pane and Analytics Pane</p>
    <h4 class="minor">1.1.1&nbsp;&nbsp; Data Pane</h4>
    <p class="tight">At the top of the Data pane is a list of available data sources for the workbook. Current used data sources are coloured in Blue (if this is the main data source) or Red (if this is a secondary data source). You can see 3 big groups of fields above the data pane:</p>
    <ul class="list">
      <li><span class="g">Dimensions</span> contains the fields that have discrete and qualitative data</li>
      <li><span class="g">Measures</span> contains numerical data that can be aggregated</li>
      <li><span class="g">Parameter</span> contains dynamic values that can replace constant values in calculations, filters, and reference lines. Parameters may be present in workbooks that you edit, but you <span class="g">cannot create parameters.</span></li>
    </ul>
    <p>To build visualizations, these 3 groups of fields can be dragged and dropped from the data pane to the <span class="g">Rows</span> and <span class="g">Columns</span> shelves, the Marks card, or one of the other available shelves.</p>
    <h4 class="minor">1.1.2&nbsp;&nbsp; Analytics pane</h4>
    <p>The Analytics pane provides quick and easy access to common analytic features in Verindo. This pane includes reference lines, box plots, trend lines forecasts, and other items that can be dragged and dropped into the view from the <span class="g">Analytics</span> pane.</p>
    <p>Toggle between the <span class="g">Data</span> pane and the <span class="g">Analytics</span> pane by clicking one of the tabs at the top of the Side Bar</p>
  </div>
  <div class="page-num page-num--green" style="left:755px;top:518px">5</div>
</section>

<!-- Spread: pages 6 and 7 -->
<section class="spread spread--bottom">
  <div class="footer-band" role="img" aria-label="Soft band in light blue and green"></div>

  <div class="blk" style="left:27px;top:36px;width:372px">
    <h3 class="sub">b.&nbsp; TOOLBAR.</h3>
    <p>A <span class="g">toolbar</span> with options for editing the view is displayed at the top of the workspace.</p>
  </div>
  <div class="toolbar" role="img" aria-label="Screenshot of the editing toolbar icons"></div>
  <div class="blk blk--loose" style="left:27px;top:93px;width:372px">
    <p>There is a summary of the current actions for do below:</p>
    <p><span class="g">Undo/Redo:</span> Lets to undo or redo almost any type of change in the view.</p>
    <p><span class="g">Pause Updates:</span> When there is placed a field on a shelf, Verindo generates the view by querying the data source. If updates seem slow when editing the view, “Pause updates” button can be activated while making a series of edits, then turn on again.</p>
    <p><span class="g">Swap:</span> This moves the fields on the Rows shelf to the Columns shelf and vice-versa.</p>
    <p class="tight">Totals: Lets to the user to compute grand totals and subtotals for the data in a view.</p>
    <ul class="list" style="margin-left:0;margin-bottom:13.5px">
      <li><span class="g">Show Column Grand Totals</span> Adds a row showing totals for all columns in the view.</li>
      <li><span class="g">Show Row Grand Totals</span> Adds a column showing totals for all rows in the view.</li>
      <li><span class="g">Add All Subtotals</span> Inserts subtotal rows and columns in the view, if you have multiple dimensions in a column or row.</li>
      <li><span class="g">Remove All Subtotals</span> Removes subtotal rows or columns.</li>
    </ul>
    <p><span class="g">Show/Hide Labels:</span> Select to show or hide marks labels in the view.</p>
    <p><span class="g">View Size:</span> Lets to change the proportions of the view within the browser window</p>
    <p><span class="g">Worksheet:</span> Contains options for making changes at the worksheet level. Create worksheets, modify sheet names, clear sheet formatting, or clear the entire sheet.</p>
    <p><span class="g">Export:</span> The user can export to capture parts of the view for use in other applications.</p>
    <p><span class="g">Show Me:</span> Opens a control that shows a range of visualization types that can be used in Verindo. Verindo uses the data in the current view to determine which visualization types to make available.</p>
  </div>
  <div class="page-num page-num--blue" style="left:356px;top:524px">6</div>

  <div class="blk" style="left:421px;top:39px;width:370px">
    <h3 class="sub">c.&nbsp; Columns and Rows.</h3>
  </div>
  <div class="blk" style="left:421px;top:58px;width:355px">
    <p class="tight">All views included in verindo have their structure arranged by Columns and Rows. The user can modify this structure by different one.</p>
    <p class="tight">By dragging fields to the Columns or Rows shelf, new columns or rows are included to the table. There can be dragged multiple fields to either shelf.</p>
    <p>Discrete values (typically, dimensions) are displayed in blue on the Columns and Row shelves; continuous values (typically, measures) are displayed in green.</p>
    <p>There is also a drop down menu in each field included at Columns or Rows pane. This menu changes his options depending on the type of field where is activated.</p>
  </div>
  <div class="label" style="left:445px;top:164px">DIMENSION</div>
  <div class="shot shot--menu" style="left:445px;top:174px;width:101px;height:82px" role="img" aria-label="Screenshot of the dimension field drop-down menu"></div>
  <div class="label" style="left:603px;top:164px">MEASURE</div>
  <div class="shot shot--menu" style="left:603px;top:180px;width:131px;height:166px" role="img" aria-label="Screenshot of the measure field drop-down menu"></div>
  <div class="blk" style="left:421px;top:383px;width:355px">
    <ul class="list" style="margin-left:0">
      <li><span class="g">Include in Tooltip (Measure)</span><br><span style="display:block;margin-left:6px">By default, all fields on the Columns and Rows shelf are included in the tooltips that appear when the mouse is moved over one or more marks in the view. Un-checking this option will remove a field from tooltips.</span></li>
      <li><span class="g">Show Filter (Dimension and Measure)</span><br><span style="display:block;margin-left:6px">This option is used for add a filter for this field to the view. Users will then be able to specify which data to include and exclude for this dimension or measure.</span></li>
    </ul>
  </div>
  <div class="page-num page-num--green" style="left:755px;top:524px">7</div>
</section>

</body>
</html>
```